Business Card Design Project

Our slogan is "Built for the wild" and we are after something creative and different to go with our company image.

Criteria:
The business card will not be a standard size but it must be small or big enough to fit in a wallet.
It will be double sided
It will have our colours and the design will be based around our logo (attached)
No fancy text just clean sharp easy to read. we have been using the stag sans book font type so this or similar type is preferable (we are not locked in a font type.

For more information about us, please visit out website at www.tovelmarsh.com.au

Target Market(s)

outdoor and recreational industry/market

Industry/Entity Type

Business

Requirements
Must have
• Logo
Slogan
website
contact details (phone and email)
Name and Position
social media facebook and youtube

```html
<!DOCTYPE html>
<html lang="en">
<head>
<meta charset="utf-8">
<title>Tovel — Business Card</title>
<link rel="stylesheet" href="https://fonts.googleapis.com/css2?family=Josefin+Sans:wght@300;400&family=Oswald:wght@500&display=swap">
<style>
  :root {
    --bg: #e9e6e2;
    --card: #1b1a1a;
    --card-glow: #2a2828;
    --orange: #e4582b;
    --white: #f4f2ef;
    --grey: #b9b5b1;
  }
  * { box-sizing: border-box; margin: 0; padding: 0; }
  html, body { width: 1200px; height: 900px; overflow: hidden; }
  body {
    background: var(--bg);
    position: relative;
    font-family: "Josefin Sans", "Helvetica Neue", Arial, sans-serif;
  }
  .card {
    position: absolute;
    top: 165px;
    width: 440px;
    height: 570px;
    background: var(--card);
    overflow: hidden;
    box-shadow: 0 10px 28px rgba(0,0,0,0.18);
  }
  .card--front { left: 120px; }
  .card--back {
    left: 640px;
    background: radial-gradient(circle at 50% 45%, var(--card-glow) 0%, var(--card) 70%);
  }

  /* Front side */
  .holder { position: absolute; left: 40px; top: 48px; }
  .holder__name { color: var(--orange); font-weight: 300; font-size: 25px; letter-spacing: 0.5px; }
  .holder__role { color: var(--grey); font-weight: 300; font-size: 12px; margin-top: 4px; }

  .contacts { position: absolute; left: 40px; top: 160px; list-style: none; }
  .contacts li {
    display: flex; align-items: center; gap: 8px;
    color: var(--white); font-weight: 300; font-size: 12.5px;
    margin-bottom: 7px;
  }
  .contacts svg { width: 13px; height: 13px; flex: none; }

  .name-vertical {
    position: absolute;
    left: 338px; top: 300px;
    width: 270px;
    transform: rotate(-90deg);
    transform-origin: top left;
  }
  .brand-name { color: var(--white); font-weight: 300; font-size: 64px; letter-spacing: 4px; line-height: 1; }
  .tagline {
    font-family: "Oswald", "Arial Narrow", sans-serif;
    font-weight: 500; text-transform: uppercase;
    color: var(--white); font-size: 14px; letter-spacing: 2.6px; line-height: 1.2;
  }

  .front-arc { position: absolute; left: 0; top: 0; }

  /* Back side */
  .brand-block {
    position: absolute; left: 0; right: 0; top: 230px;
    display: flex; flex-direction: column; align-items: center;
  }
  .brand-row { display: flex; align-items: center; gap: 18px; }
  .brand-row .brand-name { font-size: 60px; }
  .brand-dot { width: 26px; height: 26px; flex: none; }
  .brand-block .tagline { font-size: 13.5px; margin-top: 22px; }
</style>
</head>
<body>

<section class="card card--front" aria-label="Card front">
  <svg class="front-arc" width="440" height="570" aria-hidden="true">
    <circle cx="300" cy="470" r="175" fill="none" stroke="var(--orange)" stroke-width="6"/>
  </svg>

  <div class="holder">
    <p class="holder__name">Aaron Pell</p>
    <p class="holder__role">Manager</p>
  </div>

  <ul class="contacts">
    <li>
      <svg viewBox="0 0 14 14" aria-hidden="true"><circle cx="7" cy="7" r="6" fill="none" stroke="var(--orange)" stroke-width="1.2"/><path d="M5 4.2 L6 6 L5.4 6.6 Q6.4 8.2 7.6 8.8 L8.2 8.2 L10 9.2 L9.4 10.2 Q6.6 10 4.2 6 Z" fill="var(--orange)"/></svg>
      5120 3388
    </li>
    <li>
      <svg viewBox="0 0 14 14" aria-hidden="true"><rect x="1.5" y="3" width="11" height="8" fill="none" stroke="var(--orange)" stroke-width="1.2"/><path d="M1.5 3 L7 7.5 L12.5 3" fill="none" stroke="var(--orange)" stroke-width="1.2"/></svg>
      aaronpell@tovelmarsh.com.au
    </li>
    <li>
      <svg viewBox="0 0 14 14" aria-hidden="true"><circle cx="7" cy="7" r="5.6" fill="none" stroke="var(--orange)" stroke-width="1.2"/><ellipse cx="7" cy="7" rx="2.4" ry="5.6" fill="none" stroke="var(--orange)" stroke-width="1"/><line x1="1.4" y1="7" x2="12.6" y2="7" stroke="var(--orange)" stroke-width="1"/></svg>
      http://www.tovelmarsh.com.au
    </li>
    <li>
      <svg viewBox="0 0 14 14" aria-hidden="true"><rect x="1.5" y="1.5" width="11" height="11" fill="var(--orange)"/></svg>
      https://www.linkpage.com.au/TovelMarsh
    </li>
  </ul>

  <div class="name-vertical">
    <p class="brand-name">TOVEL</p>
    <p class="tagline">Built for the wild</p>
  </div>
</section>

<section class="card card--back" aria-label="Card back">
  <div class="brand-block">
    <div class="brand-row">
      <svg class="brand-dot" viewBox="0 0 26 26" aria-hidden="true">
        <circle cx="13" cy="13" r="11" fill="none" stroke="var(--orange)" stroke-width="3"/>
      </svg>
      <p class="brand-name">TOVEL</p>
    </div>
    <p class="tagline">Built for the wild</p>
  </div>
</section>

</body>
</html>
```